Covid-19 Mortgage Housing Market Coaching

I need a one page 8.5 x 11 printable infographic to describe the following:
Housing and Mortgage Market Coach
Through your Employer Home-ownership Benefit
The Coronavirus has resulted in an unprecedented Government coordination to reduce the spread of the virus, as such, has altered the way we live and work.
As each of us looks to the potential impact of the Coronavirus to our financial stability, it can be difficult to obtain trusted information to help make sound financial decisions.
As part of your employee home ownership program through your employer, you have access to this educational coaching on the below topics:
• What is happening in the stock market and why it is happening.
• Motivation behind Feds cutting rates and how that translates to the lending market.
• Discuss the future of interest rates.
• Discuss the future of the housing market. How will the spring and summer housing markets be effected?
• Everyone says to refinance now. Is that really in my best interest? Learn how to do a refinance analysis and determine if refinancing is right for you.
Having a better understanding of what is happening in the financial markets, with interest rates and the housing market can help you successfully navigate this rapidly evolving situation.
Please be sure that our phone number is prominently displayed 1-800-555-0182 and our web address www.lanternroofguild.com

```html
<!DOCTYPE html>
<html lang="en">
<head>
<meta charset="utf-8">
<title>Housing &amp; Mortgage Market Coach</title>
<link href="https://fonts.googleapis.com/css2?family=Lato:wght@400;700;900&family=Oswald:wght@500;600&display=swap" rel="stylesheet">
<style>
  :root{
    --navy:#0d2640;
    --navy-deep:#053865;
    --teal:#1b7b8c;
    --teal-mid:#3aa1b2;
    --teal-dark:#1a7a8a;
    --green:#7cc242;
    --green-dark:#6db22a;
    --green-light:#a6d65a;
    --mist:#ecefef;
    --ink:#1d1d1d;
    --page:#c9cbd0;
    --white:#ffffff;
  }
  html,body{margin:0;padding:0;width:1200px;height:1200px;overflow:hidden;background:var(--page);}
  .flyer{
    position:absolute;left:177px;top:53px;width:950px;height:1230px;
    transform:scale(0.889);transform-origin:0 0;
    background:var(--white);font-family:"Lato",sans-serif;color:var(--ink);
    box-shadow:0 6px 20px rgba(0,0,0,.25);overflow:hidden;
  }
  .abs{position:absolute;}
  /* header */
  .header-top{left:0;top:0;width:950px;height:12px;background:var(--navy);}
  .header-panel{left:0;top:0;width:950px;height:155px;}
  .brand{left:24px;top:62px;display:flex;align-items:center;gap:14px;}
  .brand-mark{width:34px;height:34px;background:var(--green);}
  .brand-name{font-weight:700;font-size:34px;color:var(--teal);letter-spacing:-.5px;}
  .brand-tag{left:72px;top:110px;font-size:17px;color:#333;}
  .title{right:33px;top:30px;text-align:right;font-family:"Oswald",sans-serif;font-weight:600;line-height:46px;font-size:48px;letter-spacing:.5px;}
  .title .line-white{color:var(--white);}
  .title .line-green{color:var(--green);}
  /* benefit band */
  .benefit{left:0;top:153px;width:950px;height:42px;background:var(--teal);}
  .benefit-rule{left:0;top:171px;width:378px;height:4px;background:var(--white);}
  .benefit-text{right:33px;top:160px;font-weight:700;font-size:21px;color:var(--white);}
  /* intro */
  .intro{left:0;top:195px;width:950px;height:193px;background:var(--mist);box-shadow:0 3px 4px rgba(0,0,0,.08);}
  .virus-art{left:268px;top:220px;width:160px;height:75px;border-radius:40px;background:#4fae9e;opacity:.75;}
  .arrow{left:445px;top:243px;}
  .finance-art{left:522px;top:218px;width:92px;height:85px;background:#dfe3e3;border:2px solid #222;border-radius:6px;box-sizing:border-box;}
  .intro-text{left:38px;top:312px;width:878px;font-size:16.5px;line-height:21px;text-align:justify;}
  /* topics */
  .topics-head{left:0;top:416px;width:950px;text-align:center;font-weight:700;font-size:20px;line-height:25px;color:var(--navy);text-transform:uppercase;}
  .topics-head .accent{color:var(--teal);}
  .topics-rule{left:92px;top:468px;width:772px;height:3px;background:var(--green);}
  .house{left:0;top:480px;}
  .icon-slot{width:72px;height:70px;border:3px solid rgba(255,255,255,.9);border-radius:10px;box-sizing:border-box;}
  .topic{left:603px;width:320px;font-size:16.5px;line-height:21px;}
  .divider{height:0;border-top:2px dotted var(--teal);}
  /* footer */
  .green-strip{left:0;top:1000px;width:950px;height:13px;background:var(--green);}
  .closing{left:0;top:1013px;width:950px;height:142px;background:var(--navy);}
  .closing-text{left:0;top:1025px;width:950px;text-align:center;color:var(--white);font-size:21px;line-height:26px;text-transform:uppercase;}
  .web-band{left:0;top:1155px;width:950px;height:75px;background:var(--teal);}
  .phone{left:303px;top:1120px;width:340px;height:48px;background:var(--green-dark);border:3px solid var(--white);border-radius:28px;box-sizing:border-box;display:flex;align-items:center;justify-content:center;gap:14px;color:var(--white);font-weight:900;font-size:31px;}
  .web{left:0;top:1180px;width:950px;text-align:center;color:var(--white);font-size:24px;}
</style>
</head>
<body>
<div class="flyer">
  <svg class="abs header-panel" width="950" height="155" viewBox="0 0 950 155">
    <rect width="950" height="155" fill="var(--navy)"/>
    <polygon points="0,12 390,12 567,153 0,153" fill="var(--white)"/>
  </svg>
  <div class="abs brand"><span class="brand-mark"></span><span class="brand-name">Lantern Roof Guild</span></div>
  <div class="abs brand-tag">Employee Home Ownership Program</div>
  <div class="abs title"><div class="line-white">HOUSING &amp; MORTGAGE</div><div class="line-green">MARKET COACH</div></div>

  <div class="abs benefit"></div>
  <div class="abs benefit-rule"></div>
  <div class="abs benefit-text">Through your Employer Home-ownership Benefit</div>

  <div class="abs intro"></div>
  <div class="abs virus-art" role="img" aria-label="Coronavirus particles illustration"></div>
  <svg class="abs arrow" width="60" height="44" viewBox="0 0 60 44" aria-hidden="true">
    <polygon points="0,14 32,14 32,0 58,22 32,44 32,30 0,30" fill="var(--green)"/>
  </svg>
  <div class="abs finance-art" role="img" aria-label="Financial chart with coin and padlock icon"></div>
  <p class="abs intro-text" style="margin:0">The Coronavirus has resulted in an unprecedented Government coordination to reduce the spread of the virus, as such, has altered the way we live and work. As each of us looks to the potential impact of the Coronavirus to our financial stability, it can be difficult to obtain trusted information to help make sound financial decisions.</p>

  <div class="abs topics-head">As part of your employee home ownership program through your employer<br>you have access to this <span class="accent">educational coaching</span> on the below topics:</div>
  <div class="abs topics-rule"></div>

  <svg class="abs house" width="600" height="520" viewBox="0 480 600 520" aria-hidden="true">
    <polygon points="312,488 45,700 580,700" fill="var(--green-light)"/>
    <polygon points="312,488 188,592 438,592" fill="var(--green-dark)"/>
    <polygon points="45,700 580,700 572,708 53,708" fill="var(--teal)"/>
    <rect x="92" y="708" width="436" height="90" fill="var(--teal-mid)"/>
    <rect x="92" y="798" width="436" height="102" fill="var(--teal-dark)"/>
    <rect x="92" y="900" width="436" height="100" fill="var(--navy-deep)"/>
  </svg>
  <div class="abs icon-slot" style="left:286px;top:518px" role="img" aria-label="Presentation board with rising chart and coin icon"></div>
  <div class="abs icon-slot" style="left:282px;top:610px" role="img" aria-label="Coupon being cut by scissors icon"></div>
  <div class="abs icon-slot" style="left:284px;top:713px" role="img" aria-label="Coins with percentage icon"></div>
  <div class="abs icon-slot" style="left:282px;top:815px" role="img" aria-label="House with dollar coin icon"></div>
  <div class="abs icon-slot" style="left:284px;top:915px" role="img" aria-label="Storefront with circulating coin icon"></div>

  <div class="abs topic" style="top:522px">What is happening in the stock market and why it is happening.</div>
  <div class="abs divider" style="left:460px;top:588px;width:470px"></div>
  <div class="abs topic" style="top:612px;left:607px">Motivation behind Feds cutting rates and how that translates to the lending market.</div>
  <div class="abs divider" style="left:588px;top:697px;width:342px"></div>
  <div class="abs topic" style="top:741px;left:608px">Discuss the future of interest rates.</div>
  <div class="abs divider" style="left:545px;top:797px;width:387px"></div>
  <div class="abs topic" style="top:818px;left:607px">Discuss the future of the housing market. How will the spring and summer housing markets be effected?</div>
  <div class="abs divider" style="left:545px;top:900px;width:387px"></div>
  <div class="abs topic" style="top:910px;left:607px">Everyone says to refinance now. Is that really in my best interest? Learn how to do a refinance analysis and determine if refinancing is right for you.</div>

  <div class="abs green-strip"></div>
  <div class="abs closing"></div>
  <div class="abs closing-text">Having a better understanding of what is happening in the<br>financial markets, with interest rates and the housing market<br>can help you successfully navigate this rapidly evolving situation</div>
  <div class="abs web-band"></div>
  <div class="abs phone">
    <svg width="30" height="30" viewBox="0 0 24 24" aria-hidden="true"><path d="M6.6 10.8a15.1 15.1 0 0 0 6.6 6.6l2.2-2.2c.3-.3.7-.4 1-.2 1.1.4 2.3.6 3.6.6.6 0 1 .4 1 1V20c0 .6-.4 1-1 1C10.6 21 3 13.4 3 4c0-.6.4-1 1-1h3.5c.6 0 1 .4 1 1 0 1.3.2 2.5.6 3.6.1.3 0 .7-.2 1z" fill="var(--white)"/></svg>
    <span>1-800-555-0182</span>
  </div>
  <div class="abs web">www.lanternroofguild.com</div>
</div>
</body>
</html>
```